Stationary design for a bidet toilet seat
Vellora Bidets
Stationary design for a bidet toilet seat  - Health
Creative Brief
Bright & Fun-filled
Tobias Merrick III
Marketing Agent
418 Westmere Ave. Suite 203 Houston, TX 77024
vellorabidets@quillpost-mail.com
My logo was done by Quorvan designs

```html
<!DOCTYPE html>
<html lang="en">
<head>
<meta charset="utf-8">
<title>Vellora Bidets – Business Card</title>
<link href="https://fonts.googleapis.com/css2?family=Cinzel:wght@500&family=Libre+Baskerville&display=swap" rel="stylesheet">
<style>
  :root{
    --stage:#8c8d8f;
    --brand-blue:#2f7fcb;
    --brand-blue-dark:#2469b0;
    --brand-green:#5c9a2c;
    --paper:#ffffff;
    --ink:#3a3a3a;
  }
  html,body{margin:0;padding:0;overflow:hidden;}
  body{width:1200px;height:908px;background:var(--stage);position:relative;}
  .card{position:absolute;width:540px;height:310px;border-radius:22px;box-shadow:0 6px 18px rgba(0,0,0,.25);overflow:hidden;}
  .card-front{left:40px;top:299px;background:linear-gradient(135deg,var(--brand-blue) 0%,var(--brand-blue-dark) 100%);}
  .card-back{left:620px;top:299px;background:var(--paper);}
  .logo{position:absolute;display:flex;align-items:center;gap:12px;white-space:nowrap;font-family:"Cinzel",serif;font-weight:500;letter-spacing:2px;}
  .logo-dot{flex:none;width:44px;height:44px;border-radius:50%;}
  .card-front .logo{left:50%;top:50%;transform:translate(-50%,-50%);color:var(--paper);font-size:30px;}
  .card-front .logo-dot{background:var(--paper);}
  .card-back .logo{left:36px;bottom:50px;gap:10px;color:var(--brand-green);font-size:17px;letter-spacing:1.5px;}
  .card-back .logo-dot{width:30px;height:30px;background:var(--brand-blue);}
  .contact{position:absolute;left:300px;top:44px;width:220px;font-family:"Libre Baskerville",serif;color:var(--ink);}
  .contact-name{font-family:"Cinzel",serif;font-weight:500;color:var(--brand-green);font-size:18px;margin:0;letter-spacing:1px;white-space:nowrap;}
  .contact-role{font-family:"Cinzel",serif;color:var(--brand-blue);font-size:11px;margin:4px 0 40px;letter-spacing:1px;}
  .contact-address{font-size:11px;line-height:1.5;margin:0 0 14px;}
  .contact-line{display:flex;align-items:center;gap:7px;font-size:11px;line-height:1.7;margin:0;white-space:nowrap;}
  .contact-line svg{flex:none;}
</style>
</head>
<body>
  <div class="card card-front">
    <div class="logo"><span class="logo-dot"></span>VELLORA BIDETS</div>
  </div>

  <div class="card card-back">
    <div class="logo"><span class="logo-dot"></span>VELLORA BIDETS</div>
    <div class="contact">
      <p class="contact-name">TOBIAS MERRICK III</p>
      <p class="contact-role">MARKETING AGENT</p>
      <p class="contact-address">418 Westmere Ave.<br>Suite 203<br>Houston, TX 77024</p>
      <p class="contact-line">
        <svg width="12" height="12" viewBox="0 0 12 12"><circle cx="6" cy="6" r="6" fill="var(--brand-green)"/><path d="M4 3.2l1 1.6-.6.7a4 4 0 0 0 2.1 2.1l.7-.6 1.6 1-.5 1a5.5 5.5 0 0 1-5.3-5.3z" fill="#fff"/></svg>
        555-014-2230
      </p>
      <p class="contact-line">
        <svg width="12" height="12" viewBox="0 0 12 12"><circle cx="6" cy="6" r="6" fill="var(--brand-green)"/><path d="M4 3.2l1 1.6-.6.7a4 4 0 0 0 2.1 2.1l.7-.6 1.6 1-.5 1a5.5 5.5 0 0 1-5.3-5.3z" fill="#fff"/></svg>
        555-014-7781
      </p>
      <p class="contact-line">
        <svg width="12" height="12" viewBox="0 0 12 12"><circle cx="6" cy="6" r="6" fill="var(--brand-green)"/><rect x="3" y="4" width="6" height="4.2" fill="none" stroke="#fff" stroke-width=".9"/><path d="M3 4l3 2.3L9 4" fill="none" stroke="#fff" stroke-width=".9"/></svg>
        vellorabidets@quillpost-mail.com
      </p>
    </div>
  </div>
</body>
</html>
```